Bright acorns day nursery pkr limited

we would like create a website that can be updated by us easily as we have regular changes to what we provide and need. we would like something that is classy but also appealing from a child's aspect. we would be looking to add our own logo and our edvarn logo both attached, if you guys can create it and we will work with the preferred choice to add all the text.
We would like the links to nest ledger, edvarn report and our chatterly feed on the front page

we are looking for a website for our childcare business we have 2 nurseries that we would like one website.
showing our opening hours, price list, policies etc as well as photos, description of our day, staff photos and their training accreditation's.

Target Market(s)

Families

Industry/Entity Type

Childcare

Number of Pages Required

5+ page

Font styles to use
Serif

Colors

Designer to choose colors to be used in the design.

Requirements
Must have
• links to social media and other websites, photographs, links to download registration forms etc, parents able to leave reviews. zarloo charts link, job opportunities
Nice to have
• facilities to take payments

```html
<!DOCTYPE html>
<html lang="en">
<head>
<meta charset="utf-8">
<title>Bright Acorns Day Nursery</title>
<link rel="stylesheet" href="https://fonts.googleapis.com/css2?family=Dancing+Script:wght@600;700&family=Poppins:wght@400;500;600&family=Roboto:wght@400;500&display=swap">
<style>
:root{
  --navy:#0b3b82;
  --green:#4aad43;
  --green-light:#6cc463;
  --pink:#d5137f;
  --ink:#555;
  --muted:#7d7d7d;
  --grey-band:#dedede;
  --grey-strip:#eeeeee;
  --white:#fff;
}
*{box-sizing:border-box;margin:0;padding:0}
html,body{width:1200px;height:2616px;overflow:hidden;background:var(--white)}
body{font-family:'Poppins',sans-serif;color:var(--ink);position:relative}
.abs{position:absolute}
.script{font-family:'Dancing Script',cursive;font-weight:700}

/* header */
.topbar{left:0;top:0;width:1200px;height:31px;background:var(--navy);color:var(--white);font-family:'Roboto',sans-serif;font-size:12px;display:flex;align-items:center;justify-content:flex-end;gap:18px;padding-right:40px}
.topbar strong{font-size:14px;font-weight:500}
.brand{left:105px;top:0;width:144px;height:88px;background:var(--white);display:flex;align-items:center;justify-content:center;gap:8px;padding:0 8px}
.brand-dot{width:14px;height:14px;background:var(--pink);flex:none}
.brand-name{font-family:'Poppins',sans-serif;font-weight:600;font-size:12px;line-height:1.25;color:var(--navy);text-align:left}
.nav{top:52px;left:375px;display:flex;gap:0;font-family:'Roboto',sans-serif;font-size:14px;color:#333}
.nav a{color:inherit;text-decoration:none;margin-right:52px}

/* hero */
.hero{left:0;top:91px;width:1200px;height:432px;background:linear-gradient(90deg,#d9cbb8 0%,#b79a7a 35%,#7a5a43 60%,#5b4032 100%)}
.hero-copy{right:60px;top:140px;width:560px;text-align:center;color:var(--white)}
.hero-copy h1{font-size:42px;line-height:1.1}
.hero-copy p{font-size:23px;line-height:1.75;margin-top:8px;letter-spacing:.5px}
.btn-outline{display:inline-block;margin-top:18px;border:2px solid var(--white);padding:8px 34px;font-size:17px;color:var(--white)}

/* day */
.day-title{left:98px;top:565px;color:var(--green);font-size:38px}
.day-sub{left:98px;top:625px;color:#666;font-size:28px;line-height:45px;width:600px}
.day-text{left:98px;top:725px;width:572px;font-size:11px;line-height:22px;color:var(--muted)}
.btn-pink{left:98px;top:863px;width:148px;height:40px;background:var(--pink);color:var(--white);font-size:17px;font-weight:500;display:flex;align-items:center;justify-content:center}
.day-photo{left:705px;top:558px;width:392px;height:364px;background:linear-gradient(160deg,#e8e2da,#b9a28a 60%,#6d7a92)}
.day-frame{left:720px;top:573px;width:362px;height:334px;border:1px dashed rgba(255,255,255,.9)}

/* price */
.price{left:0;top:952px;width:1200px;height:530px;background:var(--green);color:var(--white)}
.price h2{position:absolute;left:0;width:1200px;top:30px;text-align:center;font-size:32px}
.price-intro{position:absolute;left:172px;top:84px;width:856px;text-align:center;font-size:11px;line-height:21px}
.price-table{position:absolute;left:174px;top:166px;width:876px;border-collapse:collapse;font-family:'Poppins',sans-serif}
.price-table th{background:var(--green-light);height:99px;font-weight:500;font-size:15px;line-height:19px}
.price-table td{height:70px;text-align:center;font-size:15px;font-weight:500;border-top:1px solid rgba(255,255,255,.2)}
.price-table tr:last-child td{height:82px}
.price-table td.label{font-size:20px}
.price-table td small{display:block;font-size:9px;font-weight:500}
.price-table{border:1px solid rgba(255,255,255,.25)}
.price-note{position:absolute;left:0;width:1200px;top:446px;text-align:center;font-size:13px;line-height:28px;font-weight:500}

/* team */
.team-title{left:0;width:1200px;top:1510px;text-align:center;color:var(--green);font-size:30px}
.team-text{left:300px;width:600px;top:1556px;text-align:center;font-size:11px;line-height:24px;color:var(--muted)}
.member{top:1622px;width:276px;height:258px}
.member-1{left:153px;background:linear-gradient(160deg,#c9b8a8,#8f7e70)}
.member-2{left:466px;background:linear-gradient(160deg,#b0a79e,#7d736b)}
.member-3{left:785px;background:linear-gradient(160deg,#cfcfcf,#8b8b8b)}
.member-name{left:466px;width:276px;top:1790px;text-align:center;color:var(--white);font-size:22px;font-weight:600;letter-spacing:2px}

/* gallery */
.gallery{left:0;top:1924px;width:1200px;height:362px;background:var(--grey-band)}
.gallery-title{left:101px;top:1948px;color:var(--green);font-size:32px}
.dots{left:704px;top:1963px;display:flex;gap:3px}
.dots span{width:9px;height:9px;border:2px solid #777;border-radius:50%}
.shot{top:2004px;width:307px;height:242px}
.shot-1{left:99px;background:linear-gradient(150deg,#4c7a5e,#b8474a 60%,#3c5c8f)}
.shot-2{left:434px;background:linear-gradient(150deg,#c79d86,#b78a7a 55%,#5e6e8a)}
.feed{left:780px;top:1988px;width:321px;height:265px;background:var(--white);border:1px solid #c6cde0;font-family:'Roboto',sans-serif}
.feed-head{height:36px;background:#eef1f8;border-bottom:1px solid #d6dbe8;font-family:'Dancing Script',cursive;font-weight:700;font-size:17px;color:#333;padding:6px 14px}
.feed-page{position:absolute;left:14px;top:50px;display:flex;gap:8px;width:292px}
.sq{width:22px;height:22px;background:#ccd3e3;flex:none}
.feed-page b{font-size:11px;color:var(--navy);font-weight:500;display:block}
.feed-page i{font-style:normal;font-size:9px;color:#888}
.like{position:absolute;right:14px;top:50px;border:1px solid #bbb;font-size:9px;padding:3px 6px;color:#333;background:#f6f6f6}
.post{position:absolute;left:14px;top:108px;width:292px;font-size:9px;color:#333;line-height:12px}
.post b{color:var(--navy);font-weight:500}
.post p{margin-top:8px}
.post em{font-style:normal;color:#4b67a1;display:block;margin-top:6px}
.feed-foot{position:absolute;left:14px;bottom:10px;font-size:9px;color:#4b67a1;display:flex;gap:5px;align-items:center;border-top:1px solid #ddd;padding-top:6px;width:250px}
.feed-foot span{width:10px;height:10px;background:#4b67a1}

/* partners */
.partners{left:0;top:2286px;width:1200px;height:135px;background:var(--grey-strip)}
.partner{top:2318px;background:#3a3a3a}
.p1{left:123px;width:180px;height:70px;border-radius:6px;background:#9a9a9a}
.p2{left:410px;width:200px;height:70px;border-radius:6px}
.p3{left:733px;top:2315px;width:76px;height:76px;border-radius:50%;background:#bdbdbd}
.p4{left:958px;top:2305px;width:104px;height:104px;border-radius:50%;background:#111}

/* footer */
.footer{left:0;top:2421px;width:1200px;height:195px;background:var(--navy);color:var(--white)}
.cert{top:2445px;width:64px;height:66px;background:#1d2f6b;border:2px solid #2c4ea8}
.c1{left:385px}
.c2{left:513px}
.nest{left:637px;top:2447px;width:146px;height:62px;background:var(--white);display:flex;align-items:center;justify-content:center;font-weight:600;font-size:17px;color:var(--green)}
.foot-nav{left:0;width:1200px;top:2543px;display:flex;justify-content:center;font-size:14px;font-weight:500}
.foot-nav a{color:var(--white);text-decoration:none;margin:0 40px}
.copy{left:0;width:1200px;top:2583px;text-align:center;font-size:13px;font-weight:500}
</style>
</head>
<body>

<header>
  <div class="abs topbar"><strong>Openning Hours</strong><span>Mon - Sat : 8 am To 4 pm</span><span>Sunday Holiday</span></div>
  <div class="abs brand"><span class="brand-dot"></span><span class="brand-name">Bright Acorns<br>Day Nursery</span></div>
  <nav class="abs nav"><a>About Us</a><a>Programs</a><a>Centres</a><a>News &amp; Event</a><a>Parent Corner</a><a>Career</a><a>Contact</a></nav>
</header>

<section>
  <div class="abs hero" role="img" aria-label="Photo of a young child drawing with crayons at a table"></div>
  <div class="abs hero-copy" style="top:231px">
    <h1 class="script">Enhance Your Child's Skill With Us</h1>
    <p>Knowledge, Creativity, And Leadership Guide<br>Our Every Action</p>
    <span class="btn-outline">Contact Us Today</span>
  </div>
</section>

<section>
  <h2 class="abs script day-title">Description Of Our Day</h2>
  <p class="abs script day-sub">We Are Committed In Creating The Future<br>Leaders Of Our Country</p>
  <p class="abs day-text">Lorem Ipsum is simply dummy text of the printing and typesetting industry. Lorem Ipsum has been the industry's standard dummy text ever since the 1500s, when an unknown printer took a galley of type and scrambled it to make a type specimen book. It has survived not only five centuries, but also the leap into electronic typesetting, remaining essentially unchanged.Lorem Ipsum is simply dummy text of the printing and typesetting industry. Lorem Ipsum has been the industry's standard dummy text ever since the 1500s, when an unknown printer took a galley of type and scrambled.</p>
  <div class="abs btn-pink">Our Policies</div>
  <div class="abs day-photo" role="img" aria-label="Photo of a toddler in a pilot cap playing with a toy plane"></div>
  <div class="abs day-frame"></div>
</section>

<section class="abs price">
  <h2 class="script">Check Out Our Price List</h2>
  <p class="price-intro">Lorem Ipsum is simply dummy text of the printing and typesetting industry. Lorem Ipsum has been the industry's standard dummy text ever since the 1500sLorem Ipsum is simply dummy text of the printing and typesetting industry. Lorem Ipsum has been the industry's standard dummy text ever since the 1500sLorem Ipsum is simply dummy text of the printing and typesetting industry. Lorem Ipsum</p>
  <table class="price-table">
    <colgroup><col style="width:140px"><col style="width:150px"><col style="width:130px"><col style="width:150px"><col></colgroup>
    <tr><th></th><th>Half day<br>8am-1pm or<br>1pm-6pm</th><th>Full day<br>(7.30-6pm)</th><th>Full time<br>Mon- Fri<br>7.30-6pm</th><th>Full time<br>funded children<br>3+ years</th></tr>
    <tr><td class="label">Under 2's</td><td>£26</td><td>£40</td><td>£168</td><td>xxxxxxxxxx</td></tr>
    <tr><td class="label">2-5's</td><td>£25</td><td>£38</td><td>£161<small>(Funded children in holidays)</small></td><td>£130<small>During term time</small></td></tr>
  </table>
  <p class="price-note">Fees include breakfast (full day/full time only). A light snack each session, nappies and wipes.<br>Meals can be offered for an additional charge (£2.50 per meal, per day). &nbsp;Please see a member of staff!</p>
</section>

<section>
  <h2 class="abs script team-title">Meet Our Team For Your Child</h2>
  <p class="abs team-text">Lorem Ipsum is simply dummy text of the printing and typesetting industry. Lorem Ipsum has been the industry's standard dummy text ever since the 1500s, when an unknown printer</p>
  <div class="abs member member-1" role="img" aria-label="Staff photo of a smiling team member with glasses"></div>
  <div class="abs member member-2" role="img" aria-label="Staff photo of a smiling team member"></div>
  <div class="abs member member-3" role="img" aria-label="Staff photo of a smiling male team member"></div>
  <div class="abs member-name">MARLA PENN</div>
</section>

<section>
  <div class="abs gallery"></div>
  <h2 class="abs script gallery-title">Our Gallery</h2>
  <div class="abs dots"><span></span><span></span><span></span></div>
  <div class="abs shot shot-1" role="img" aria-label="Gallery photo of a teacher reading to children"></div>
  <div class="abs shot shot-2" role="img" aria-label="Gallery photo of children gathered around a teacher with a book"></div>
  <aside class="abs feed">
    <div class="feed-head">Recent Activity</div>
    <div class="feed-page"><span class="sq"></span><div><b>Bright acorns day nursery pkr limited</b><i>6 July at 15:25</i></div></div>
    <span class="like">Like Page</span>
    <div class="post">
      <b>Bright acorns day nursery pkr limited</b><br><span style="color:#888">6 July at 15:25</span>
      <p>CALLING ALL PARENTS/CARERS WITH 2,3 &amp; 4 YEAR OLDS!! DON'T FORGET TIME IS RUNNING OUT TO APPLY FOR FUNDING/SUPPORT WITH CHILDCARE FEE'S FROM SEPT 1?! VISIT THE L...</p>
      <em>See more</em>
    </div>
    <div class="feed-foot"><span></span>chatterly social plugin</div>
  </aside>
</section>

<section>
  <div class="abs partners"></div>
  <div class="abs partner p1" role="img" aria-label="Partner accreditation badge"></div>
  <div class="abs partner p2" role="img" aria-label="Partner nursery badge"></div>
  <div class="abs partner p3" role="img" aria-label="Accreditation seal"></div>
  <div class="abs partner p4" role="img" aria-label="Accredited nursery seal"></div>
</section>

<footer>
  <div class="abs footer"></div>
  <div class="abs cert c1" role="img" aria-label="edvarn outstanding certificate"></div>
  <div class="abs cert c2" role="img" aria-label="edvarn outstanding certificate"></div>
  <div class="abs nest">nest ledger</div>
  <nav class="abs foot-nav"><a>About Us</a><a>Programs</a><a>Centres</a><a>News &amp; Event</a><a>Parent Corner</a><a>Career</a><a>Contact</a></nav>
  <p class="abs copy">©2017 Bright Acorns Day Care. All rights reserved.Terms &amp; Conditions</p>
</footer>

</body>
</html>
```